Design business card for Bright Harbour Coaching!

I am a personal development coach (like a life coach) and corporate trainer and need a professionally designed double sided business card.

It needs to contain the business logo (I'm happy for the designer to choose the layout of the logo as I am still working out the best option myself) and the following information:

Tamsin Varga
Personal Development Coach and Trainer

+61 (0)452 819 407 (written that way)
tamsin@bright-harbour.com

www.bright-harbour.com

```html
<!DOCTYPE html>
<html lang="en">
<head>
<meta charset="utf-8">
<title>Bright Harbour Coaching – Business Card</title>
<link rel="stylesheet" href="https://fonts.googleapis.com/css2?family=Cinzel:wght@400&family=Open+Sans:wght@400;600&display=swap">
<style>
  :root {
    --backdrop: #3a332f;
    --card: #0c0c0c;
    --card-edge: #1c1c1c;
    --teal: #1a9aa6;
    --silver: #c9c9c9;
    --white: #f2f2f2;
    --muted: #9a9a9a;
  }
  * { margin: 0; padding: 0; box-sizing: border-box; }
  html, body { width: 1200px; height: 900px; overflow: hidden; }
  body {
    background: var(--backdrop);
    display: flex;
    align-items: center;
    justify-content: center;
    gap: 40px;
    font-family: "Open Sans", sans-serif;
  }
  .card {
    width: 540px;
    height: 309px;
    background: var(--card);
    border: 1px solid var(--card-edge);
    position: relative;
    box-shadow: 0 14px 30px rgba(0,0,0,0.45);
  }
  .brand {
    display: flex;
    align-items: center;
    gap: 16px;
  }
  .brand-dot {
    width: 34px;
    height: 34px;
    border-radius: 50%;
    flex: none;
  }
  .brand-name {
    font-family: "Cinzel", serif;
    font-weight: 400;
    font-size: 24px;
    line-height: 1.05;
    letter-spacing: 0.5px;
    color: var(--silver);
  }
  .card-front .brand { position: absolute; left: 40px; top: 44px; }
  .card-front .brand-dot { background: var(--teal); }
  .person { position: absolute; left: 108px; top: 132px; }
  .person-name {
    color: var(--teal);
    font-weight: 600;
    font-size: 19px;
  }
  .person-role {
    color: var(--white);
    font-size: 14px;
    margin-top: 2px;
  }
  .contacts {
    list-style: none;
    position: absolute;
    left: 108px;
    top: 204px;
    color: var(--white);
    font-size: 14px;
  }
  .contacts li {
    display: flex;
    align-items: center;
    gap: 10px;
    height: 24px;
  }
  .contacts svg { width: 12px; height: 12px; fill: var(--teal); flex: none; }
  .card-back .brand { position: absolute; left: 70px; top: 112px; }
  .card-back .brand-dot { background: var(--silver); }
  .card-back .web {
    position: absolute;
    left: 170px;
    top: 180px;
    color: var(--muted);
    font-size: 13px;
  }
</style>
</head>
<body>
  <section class="card card-front" aria-label="Card front">
    <div class="brand">
      <span class="brand-dot"></span>
      <span class="brand-name">Bright Harbour<br>Coaching</span>
    </div>
    <div class="person">
      <p class="person-name">Tamsin Varga</p>
      <p class="person-role">Personal Development Coach and Trainer</p>
    </div>
    <ul class="contacts">
      <li>
        <svg viewBox="0 0 12 12" aria-hidden="true"><path d="M2.5 0.5 L4.5 3 L3.5 4.5 Q5 7.2 7.5 8.5 L9 7.5 L11.5 9.5 L10 11.5 Q4.5 11 0.5 2 Z"/></svg>
        +61 (0)452 819 407
      </li>
      <li>
        <svg viewBox="0 0 12 12" aria-hidden="true"><path d="M0 2 H12 V10 H0 Z M0.8 2.6 L6 6.6 L11.2 2.6 V3.6 L6 7.6 L0.8 3.6 Z" fill-rule="evenodd"/></svg>
        tamsin@bright-harbour.com
      </li>
      <li>
        <svg viewBox="0 0 12 12" aria-hidden="true"><path d="M4.5 7.5 L7.5 4.5 M3 6 L1.5 7.5 Q0 9 1.5 10.5 Q3 12 4.5 10.5 L6 9 M6 3 L7.5 1.5 Q9 0 10.5 1.5 Q12 3 10.5 4.5 L9 6" stroke="#1a9aa6" stroke-width="1.6" fill="none"/></svg>
        www.bright-harbour.com
      </li>
    </ul>
  </section>

  <section class="card card-back" aria-label="Card back">
    <div class="brand">
      <span class="brand-dot"></span>
      <span class="brand-name">Bright Harbour<br>Coaching</span>
    </div>
    <p class="web">www.bright-harbour.com</p>
  </section>
</body>
</html>
```